out of the box Business Card Design for a Manufacturer / Distributor

We are a manufarturer and distributor of products.
the company name is VORTANI (Pic attached)

the picture is NOT a must have on the business Card.

the Business Card should look really professional and/or special, so out of the box thinking is welcome.

there should be 2 Adresses on the Business Card for Main and Branch Office.
Email Adress, homepage, Name is required
NO Phone Number

Our working field:
Private Labeling
high Quality Production
direct distribution
warehousing
trademark registration
legal support

Main Office:
Kornblumenweg 14
08352 Wiesenbrück
Germany

Branch Office:
Daska Lane
Zarpindi
Pakistan

Names:
Lukas Feldhaus (Owner)
Imran Qureshi (Owner)

Email:
lukas@vortani-example.com
imran@vortani-example.com

homepage:
vortani-example.com

Industry/Entity Type

Manufacturer Distributer

Contact Information for Business Card

Vortani

Requirements
Must have
• Names, both office Adresses, email, homepage
Should not have
• Phone Number

```html
<!DOCTYPE html>
<html lang="en">
<head>
<meta charset="utf-8">
<title>Vortani Business Card</title>
<link href="https://fonts.googleapis.com/css2?family=Montserrat:wght@400;500&family=Arimo:wght@400;700&display=swap" rel="stylesheet">
<style>
  :root {
    --stage: #eeeeee;
    --paper: #ffffff;
    --ink: #1b1b1b;
    --cyan: #00bff0;
    --teal: #0a6f8e;
    --deep: #1b2830;
    --line: #d4d4d4;
  }
  html, body {
    margin: 0;
    padding: 0;
    overflow: hidden;
  }
  .canvas {
    position: relative;
    width: 1200px;
    height: 1200px;
    background: var(--stage);
    overflow: hidden;
  }
  .card {
    position: absolute;
    width: 610px;
    height: 348px;
    display: block;
    outline: 1px solid var(--line);
  }
  .card--front { left: 170px; top: 176px; }
  .card--back  { left: 414px; top: 600px; }

  .brand-name {
    font-family: "Montserrat", sans-serif;
    font-weight: 400;
    font-size: 40px;
    fill: var(--ink);
    letter-spacing: 0.5px;
  }
  .person-name {
    font-family: "Montserrat", sans-serif;
    font-weight: 400;
    font-size: 27px;
    fill: var(--paper);
  }
  .person-email,
  .contact-text {
    font-family: "Arimo", sans-serif;
    font-weight: 400;
    fill: var(--paper);
  }
  .person-email { font-size: 10.5px; }
  .contact-text { font-size: 12px; }
  .contact-text--small { font-size: 10px; }
  .branch-line {
    font-family: "Arimo", sans-serif;
    font-weight: 700;
    font-size: 11px;
    fill: var(--paper);
  }
  .services {
    font-family: "Arimo", sans-serif;
    font-weight: 400;
    font-size: 10.5px;
    fill: var(--ink);
    letter-spacing: 0.3px;
  }
</style>
</head>
<body>
<main class="canvas">

  <!-- Front side -->
  <svg class="card card--front" viewBox="0 0 508 290" xmlns="http://www.w3.org/2000/svg" aria-label="Business card front">
    <defs>
      <clipPath id="front-clip"><rect width="508" height="290"/></clipPath>
      <linearGradient id="front-ring" gradientUnits="userSpaceOnUse" x1="120" y1="0" x2="185" y2="0">
        <stop offset="0" stop-color="var(--cyan)"/>
        <stop offset="1" stop-color="var(--teal)"/>
      </linearGradient>
      <linearGradient id="front-arc" gradientUnits="userSpaceOnUse" x1="165" y1="0" x2="256" y2="0">
        <stop offset="0" stop-color="#0f84a5"/>
        <stop offset="1" stop-color="var(--deep)"/>
      </linearGradient>
    </defs>
    <rect class="card-paper" width="508" height="290" fill="var(--paper)"/>
    <g clip-path="url(#front-clip)">
      <path class="front-crescent" fill="url(#front-ring)" fill-rule="evenodd"
            d="M 183 145 A 175 175 0 1 1 -167 145 A 175 175 0 1 1 183 145 Z
               M 143 145 A 165 165 0 1 0 -187 145 A 165 165 0 1 0 143 145 Z"/>
      <path class="front-quarter-arc" fill="url(#front-arc)"
            d="M 256 145 L 218 145 A 210 210 0 0 1 160 290 L 209 290 A 248 248 0 0 0 256 145 Z"/>
    </g>
    <circle class="brand-dot" cx="238" cy="61" r="13" fill="var(--ink)"/>
    <text class="brand-name" x="262" y="76">VORTANI</text>
  </svg>

  <!-- Back side -->
  <svg class="card card--back" viewBox="0 0 508 290" xmlns="http://www.w3.org/2000/svg" aria-label="Business card back">
    <defs>
      <clipPath id="back-clip"><rect width="508" height="290"/></clipPath>
      <linearGradient id="back-fade" x1="0" y1="0" x2="1" y2="0">
        <stop offset="0" stop-color="var(--ink)"/>
        <stop offset="0.38" stop-color="var(--ink)"/>
        <stop offset="0.58" stop-color="var(--teal)"/>
        <stop offset="0.8" stop-color="var(--cyan)"/>
        <stop offset="1" stop-color="var(--cyan)"/>
      </linearGradient>
    </defs>
    <rect class="card-base" width="508" height="290" fill="url(#back-fade)"/>
    <g clip-path="url(#back-clip)">
      <circle class="white-ring" cx="632" cy="145" r="282" fill="var(--paper)"/>
      <circle class="service-disc" cx="563" cy="145" r="181" fill="var(--cyan)"/>
      <path class="white-quarter-arc" fill="var(--paper)"
            d="M 252 145 L 288 145 A 344 344 0 0 0 320 290 L 281 290 A 380 380 0 0 1 252 145 Z"/>
    </g>

    <line class="edge-rule" x1="13" y1="0" x2="13" y2="190" stroke="var(--paper)" stroke-width="1.4"/>

    <g class="contact-person">
      <text class="person-name" x="88" y="47">Lukas Feldhaus</text>
      <rect x="90" y="52" width="114" height="4.5" fill="var(--paper)"/>
      <text class="person-email" x="206" y="58">lukas@vortani-example.com</text>
    </g>
    <g class="contact-person">
      <text class="person-name" x="50" y="101">Imran Qureshi</text>
      <rect x="52" y="105" width="118" height="4.5" fill="var(--paper)"/>
      <text class="person-email" x="172" y="111">imran@vortani-example.com</text>
    </g>

    <g class="contact-web">
      <path d="M 8 212 L 21 218 L 8 224 L 11 218 Z" fill="var(--paper)"/>
      <text class="contact-text" x="34" y="223">vortani-example.com</text>
    </g>
    <g class="contact-address">
      <path d="M 14 256 C 10 250 8 247 8 244 A 6 6 0 0 1 20 244 C 20 247 18 250 14 256 Z" fill="none" stroke="var(--paper)" stroke-width="1.6"/>
      <circle cx="14" cy="244" r="1.8" fill="var(--paper)"/>
      <text class="contact-text contact-text--small" x="34" y="249">Kornblumenweg 14 08352 Wiesenbrück Germany</text>
      <text class="branch-line" x="34" y="266">DASKA LANE</text>
      <line x1="110" y1="256" x2="110" y2="268" stroke="var(--paper)" stroke-width="0.8"/>
      <text class="branch-line" x="114" y="266">ZARPINDI</text>
      <line x1="174" y1="256" x2="174" y2="268" stroke="var(--paper)" stroke-width="0.8"/>
      <text class="branch-line" x="178" y="266">PAKISTAN</text>
    </g>

    <g class="service-list" transform="translate(437 145) rotate(-90)">
      <text class="services" text-anchor="middle">
        <tspan x="0" y="-32">WAREHOUSING</tspan>
        <tspan x="0" y="-19">LEGAL SUPPORT</tspan>
        <tspan x="0" y="-6">PRIVATE LABELING</tspan>
        <tspan x="0" y="7">DIRECT DISTRIBUTION</tspan>
        <tspan x="0" y="20">TRADEMARK REGISTRATION</tspan>
        <tspan x="0" y="33">HIGH QUALITY PRODUCTION</tspan>
      </text>
    </g>
    <rect class="service-mark" x="366" y="143" width="3" height="3" fill="var(--ink)"/>
    <rect class="service-mark" x="492" y="143" width="3" height="3" fill="var(--ink)"/>
  </svg>

</main>
</body>
</html>
```